LinkedIn Banner Design for Asphalt & Parking Lot Company (Blacktop Harbor LLC)

I need a professional LinkedIn banner designed for my company, Blacktop Harbor LLC, based in Seattle. This banner should act as a visual “landing page header” for my profile and clearly communicate what we do within seconds.

The goal is to attract property managers, business owners, and commercial clients who are responsible for maintaining parking lots.

About the Business:
Blacktop Harbor LLC provides asphalt parking lot services including:

Sealcoating
Crack sealing
Line striping
Asphalt maintenance & repair

Website: https://blacktopharbor.net
Location: Seattle, WA

Target Audience:

Property managers
Commercial real estate owners
Facility managers
Business owners with parking lots

Main Goal of the Banner:

Instantly show what we do
Build trust and professionalism
Generate leads from profile visitors
Make people think: “This is who I call for parking lot maintenance”

Headline / Tagline (Use This or Improve It):
Helping Property Managers Protect & Maintain Their Parking Lots

Subtext (optional but recommended):
Sealcoating • Crack Sealing • Line Striping

Design Style:

Clean, bold, and modern
Professional contractor/service look
High contrast and easy to read
Not cluttered

Branding / Colors:

Orange (primary accent color from logo)
Black / dark gray (asphalt tones)
White for contrast
Match branding from website and logo

Visual Direction (IMPORTANT):
Use high-quality, realistic images such as:

Freshly sealcoated, dark black parking lot
Clean, professionally striped parking lot
Before/after transformation (if done cleanly)

The banner should visually communicate:
“We make parking lots look new and last longer”

Focus more on RESULTS than workers.

Layout Notes:

Keep important text on the center/right side (profile photo covers left side)
Must look good on desktop and mobile
Avoid placing key elements on the far left

Optional Elements:

“Serving Seattle Area”
Website: blacktopharbor.net

Deliverables:

LinkedIn banner size: 1584 x 396 px
High-resolution file
Source file (PSD or AI)

What I DON’T Want:

Generic or low-quality stock designs
Overcrowded text
Cartoon-style construction graphics

Extra Notes:
This banner is important for lead generation. It should clearly communicate services even at a quick glance.

I’m open to creative ideas that align with attracting property managers and commercial clients.

Looking forward to your designs!

```html
<!DOCTYPE html>
<html lang="en">
<head>
<meta charset="utf-8">
<title>Blacktop Harbor LLC — LinkedIn Banner</title>
<link rel="stylesheet" href="https://fonts.googleapis.com/css2?family=Arimo:ital,wght@0,400;0,700;1,700&display=swap">
<style>
  :root {
    --page-bg: #fafafa;
    --brand-orange: #ff8710;
    --ink-dark: #333333;
    --frame-light: #e4e4e2;
    --white: #ffffff;
    --worn-light: #8a8176;
    --worn-mid: #6b6156;
    --worn-earth: #7d6548;
    --worn-deep: #3f3832;
    --fresh-far: #55575b;
    --fresh-mid: #2b2c30;
    --fresh-deep: #151619;
  }
  * { margin: 0; padding: 0; box-sizing: border-box; }
  html, body {
    width: 1200px; height: 1001px; overflow: hidden;
    background: var(--page-bg);
    font-family: "Arimo", Arial, sans-serif;
  }
  .canvas { position: relative; width: 1200px; height: 1001px; }
  .banner-art { position: absolute; inset: 0; }
  .headline {
    position: absolute; left: 318px; top: 397px;
    font-size: 24px; line-height: 29px; font-weight: 700;
    color: var(--ink-dark);
  }
  .services {
    position: absolute; left: 319px; top: 498px;
    font-size: 13px; font-weight: 700; letter-spacing: 0.1px;
    color: var(--ink-dark);
  }
  .website {
    position: absolute; left: 318px; top: 546px;
    display: flex; align-items: center; gap: 4px;
    font-size: 26px; font-weight: 700;
    color: var(--ink-dark); text-decoration: none;
  }
  .website svg { width: 21px; height: 21px; margin-top: 3px; }
  .photo-label {
    position: absolute;
    font-size: 22px; font-style: italic; font-weight: 700;
    color: var(--ink-dark); text-align: center;
    background: var(--frame-light);
  }
  .photo-label.before { left: 960px; top: 324px; width: 86px; height: 28px; line-height: 28px; }
  .photo-label.after { left: 792px; top: 582px; width: 88px; height: 27px; line-height: 28px; }
  .brand-name {
    position: absolute; left: 960px; top: 514px;
    font-size: 25px; line-height: 28px; font-weight: 700;
    color: var(--white); text-transform: uppercase;
  }
</style>
</head>
<body>
<div class="canvas">
  <svg class="banner-art" width="1200" height="1001" viewBox="0 0 1200 1001">
    <defs>
      <linearGradient id="worn-asphalt" x1="0" y1="0" x2="1" y2="1">
        <stop offset="0" stop-color="var(--worn-light)"/>
        <stop offset="0.45" stop-color="var(--worn-mid)"/>
        <stop offset="0.65" stop-color="var(--worn-earth)"/>
        <stop offset="1" stop-color="var(--worn-deep)"/>
      </linearGradient>
      <linearGradient id="fresh-asphalt" x1="0" y1="0" x2="0.4" y2="1">
        <stop offset="0" stop-color="var(--fresh-far)"/>
        <stop offset="0.35" stop-color="var(--fresh-mid)"/>
        <stop offset="1" stop-color="var(--fresh-deep)"/>
      </linearGradient>
    </defs>

    <rect class="banner-band" x="30" y="324" width="1140" height="285" fill="var(--brand-orange)"/>

    <g class="dot-grid" fill="var(--frame-light)">
      <rect x="50" y="344" width="8" height="8"/><rect x="79" y="344" width="8" height="8"/><rect x="108" y="344" width="8" height="8"/><rect x="137" y="344" width="8" height="8"/>
      <rect x="50" y="367" width="8" height="8"/><rect x="79" y="367" width="8" height="8"/><rect x="108" y="367" width="8" height="8"/><rect x="137" y="367" width="8" height="8"/>
      <rect x="50" y="390" width="8" height="8"/><rect x="79" y="390" width="8" height="8"/><rect x="108" y="390" width="8" height="8"/><rect x="137" y="390" width="8" height="8"/>
      <rect x="50" y="413" width="8" height="8"/><rect x="79" y="413" width="8" height="8"/><rect x="108" y="413" width="8" height="8"/><rect x="137" y="413" width="8" height="8"/>
    </g>

    <g class="dot-corner" fill="var(--frame-light)">
      <rect x="1132" y="514" width="8" height="8"/>
      <rect x="1132" y="538" width="8" height="8"/>
      <rect x="1132" y="561" width="8" height="8"/>
      <rect x="1132" y="585" width="8" height="8"/>
      <rect x="1044" y="585" width="8" height="8"/>
      <rect x="1074" y="585" width="8" height="8"/>
      <rect x="1103" y="585" width="8" height="8"/>
    </g>

    <polygon class="photo-frame" points="774,324 1026,324 1120,478 872,478" fill="var(--frame-light)"/>
    <polygon class="photo-before" points="792,324 1012,324 1096,466 880,466" fill="url(#worn-asphalt)"
             role="img" aria-label="Before photo: cracked, crumbling parking lot asphalt with a muddy water-filled pothole"/>

    <polygon class="photo-frame" points="661,455 896,455 1004,609 776,609" fill="var(--frame-light)"/>
    <polygon class="photo-after" points="686,467 884,467 992,609 792,609" fill="url(#fresh-asphalt)"
             role="img" aria-label="After photo: freshly sealcoated jet-black parking lot with crisp new yellow stall striping"/>

    <g class="transform-arrow" fill="none" stroke="var(--white)" stroke-width="3" stroke-linecap="round" stroke-linejoin="round">
      <path d="M797 367 C 760 372, 745 405, 765 442"/>
      <path d="M752 430 L 765 443 L 771 425"/>
    </g>

    <circle class="profile-ring" cx="176" cy="562" r="114" fill="var(--frame-light)"/>
    <circle class="profile-photo" cx="176" cy="562" r="108" fill="#b9b9b9"
            role="img" aria-label="Profile photo of the company owner"/>
  </svg>

  <h1 class="headline">Helping Property Managers<br>Protect &amp; Maintain Their<br>Parking Lots</h1>
  <p class="services">SEALCOATING · CRACK SEALING · LINE STRIPING</p>
  <a class="website" href="https://blacktopharbor.net">
    <svg viewBox="0 0 24 24" fill="none" stroke="var(--ink-dark)" stroke-width="2">
      <circle cx="12" cy="12" r="10"/>
      <ellipse cx="12" cy="12" rx="4.5" ry="10"/>
      <path d="M2 12h20M4 6.5h16M4 17.5h16"/>
    </svg>
    <span>blacktopharbor.net</span>
  </a>

  <div class="photo-label before">Before</div>
  <div class="photo-label after">After</div>

  <div class="brand-name">Blacktop<br>Harbor</div>
</div>
</body>
</html>
```